Design a poster for Ellery's Dash 2023. A charity event supporting paediatric brain cancer.

We need a new poster for our event in 2023. The successful applicant will have opportunity for ongoing work with our foundation as we need a number of other deliverables once the design is finalised. We have a strong, fun and youthful brand.
Please see attached PDF showing the last 10 years of designs.
Please see attached moodboards outlining concepts for our 2023 theme. The last image of skateboarder concept is "Dusky Glow" - A retro miami vibe Juxtaposed with photo of someone from one of our previous events. Potentially posters could have multiple variants building on lots of different photos.
I have attached our brand guidelines as well as lock ups for our Ellery's Dash logos.
Whatever is created needs to be transferrable on to a number of different mediums, most importantly T-shirts, Web Banners, Billboards, Pavement Stickers, Social posts.
Our sponsor logos will remain the same.
Please only send complete designs - aligned with one of the 4 concepts provided and include all copy as per attached and include sponsors logos. Please ensure the body fonts are Brandon Grotesque and CCMatinee Idol.
Updates
Hi All, Thank you so much for all the submissions. Unfortunately after our CEO and team have reviewed the designs they are looking to go in quite a different direction than the original brief provided. I apologise for wasting your time. I have updated brief, and more specific moodboards, the last image concept is "Dusky Glow" - A retro miami vibe Juxtaposed with photo of someone from one of our previous events. Potentially posters could have multiple variants building on lots of different photos . If you would like to submit another design that would be great but if not we completely understand. Thank you again for your creative submissions.
Target Market(s)
18-35 year olds
Industry/Entity Type
Not for Profit - Fun Run Event and Party
Font styles to use
Other font styles liked:
- Fonts in Brand Guidelines - Brandon Grotesque and CCMatinee Idol
Requirements
Must have
- On Brand - colourful, focus on ALL SMILES NO MILES

```html
<!DOCTYPE html>
<html lang="en">
<head>
<meta charset="utf-8">
<title>Ellery's Dash 2023 – Poster</title>
<link rel="stylesheet" href="https://fonts.googleapis.com/css2?family=Anton&family=Figtree:wght@600;700;800&family=Oswald:wght@500&display=swap">
<style>
  :root {
    --backdrop: #eeeeec;
    --navy: #231a5b;
    --navy-deep: #1a1347;
    --sunshine: #f8cd6a;
    --pink: #ee4f7b;
    --steel-blue: #34528f;
    --sky: #5ba7da;
    --ink: #1f1a3f;
    --white: #ffffff;
    --shadow-blue: #8c93b8;
  }
  * { box-sizing: border-box; margin: 0; padding: 0; }
  html, body { width: 1200px; height: 2740px; overflow: hidden; }
  body {
    background: var(--backdrop);
    font-family: "Figtree", sans-serif;
    position: relative;
  }
  .poster {
    position: absolute;
    left: 50px; top: 634px;
    width: 1100px; height: 1471px;
    background: var(--sunshine);
    overflow: hidden;
    box-shadow: 0 18px 40px rgba(0,0,0,0.18);
  }
  .poster__sky {
    position: absolute; left: 0; top: 0; width: 100%; height: 747px;
    background: var(--navy);
  }
  .header-tag {
    position: absolute; top: 104px;
    font-weight: 700; font-size: 34px; line-height: 0.9;
    color: var(--white); text-transform: uppercase;
  }
  .header-tag strong { color: var(--sky); font-weight: 800; }
  .header-tag__line { display: block; }
  .header-tag--left { left: 92px; }
  .header-tag--right { right: 80px; text-align: right; }
  .foundation-badge {
    position: absolute; left: 460px; top: 37px;
    width: 178px; height: 178px; border-radius: 50%;
    background: var(--navy-deep);
    border: 3px solid #2f2870;
    display: flex; align-items: center; justify-content: center;
    color: var(--white); font-weight: 800; font-size: 30px;
    text-transform: uppercase; letter-spacing: 1px; text-align: center; line-height: 1;
  }
  .event-arch { position: absolute; left: 0; top: 230px; width: 1100px; height: 260px; }
  .event-arch text {
    font-family: "Anton", sans-serif; font-size: 132px; letter-spacing: 22px;
  }
  .event-arch .arch-shadow { fill: var(--shadow-blue); }
  .event-arch .arch-face { fill: var(--white); }
  .event-row {
    position: absolute; left: 0; top: 430px; width: 100%;
    display: flex; justify-content: center; align-items: center; gap: 42px;
    color: var(--white);
  }
  .event-row__side { font-family: "Oswald", sans-serif; font-size: 58px; letter-spacing: 1px; }
  .event-row__main {
    font-family: "Anton", sans-serif; font-size: 138px; letter-spacing: 30px; line-height: 1;
    text-shadow: -6px 6px 0 var(--shadow-blue);
  }
  .runners-art {
    position: absolute; left: 80px; top: 605px; width: 940px; height: 240px;
    background: linear-gradient(90deg, #e86a4a 0%, #ee4f7b 30%, #5ba7da 60%, #f3c54a 80%, #7bc0e6 100%);
    border-radius: 40px 40px 20px 20px;
    opacity: 0.9;
  }
  .info-frame {
    position: absolute; left: 49px; top: 747px; width: 999px; height: 485px;
    border: 2px solid var(--ink); border-top: none;
  }
  .info {
    position: absolute; left: 0; width: 100%; text-align: center;
    text-transform: uppercase; color: var(--ink); font-weight: 800;
  }
  .info--headline { top: 880px; font-size: 80px; color: var(--pink); line-height: 1; }
  .info--headline .amp { font-weight: 600; }
  .rule { position: absolute; left: 203px; width: 700px; height: 2px; background: var(--ink); opacity: 0.6; }
  .rule--one { top: 962px; }
  .rule--two { top: 1018px; }
  .info--date { top: 964px; font-size: 43px; }
  .info--date sup { font-size: 24px; vertical-align: 16px; }
  .info--anyday { top: 1030px; font-size: 40px; line-height: 1; }
  .info--month { top: 1068px; font-size: 66px; color: var(--steel-blue); line-height: 1; }
  .info--register { top: 1168px; font-size: 32px; font-weight: 700; }
  .web-address {
    position: absolute; left: 288px; top: 1211px; width: 550px; height: 48px;
    background: var(--navy); border: 4px solid var(--ink);
    box-shadow: inset 0 0 0 2px var(--white);
    color: var(--white); font-weight: 600; font-size: 33px; letter-spacing: 4px;
    display: flex; align-items: center; justify-content: center;
  }
  .supporters-label {
    position: absolute; top: 1288px; left: 0; width: 100%; text-align: center;
    font-weight: 700; font-size: 18px; letter-spacing: 9px; color: var(--ink);
  }
  .sponsors {
    position: absolute; top: 1340px; left: 110px; right: 110px;
    display: flex; justify-content: space-between; align-items: center;
  }
  .sponsor { display: flex; align-items: center; gap: 8px; font-weight: 800; font-size: 32px; }
  .sponsor__dot { width: 18px; height: 18px; border-radius: 50%; background: #1d9ad6; }
  .sponsor--pantrio { color: #e02a2e; }
  .sponsor--cloudnest { color: #1d9ad6; }
  .sponsor--kazemoto { color: #17449a; }
  .sponsor--signal { color: #1a1a1a; }
  .sponsor--maple { color: #2c5e3f; }
</style>
</head>
<body>
  <main class="poster">
    <div class="poster__sky"></div>

    <p class="header-tag header-tag--left"><span class="header-tag__line">Supporting</span><strong class="header-tag__line">Young Minds</strong></p>
    <div class="foundation-badge">Halden<br>Fdn</div>
    <p class="header-tag header-tag--right"><span class="header-tag__line">The <strong>#1 Disease</strong></span><strong class="header-tag__line">Killer of Young</strong></p>

    <svg class="event-arch" viewBox="0 0 1100 260" aria-label="Ellery's">
      <defs>
        <path id="arch-path" d="M90,250 Q550,-30 1010,250"/>
      </defs>
      <text class="arch-shadow" transform="translate(-7,7)"><textPath href="#arch-path" startOffset="50%" text-anchor="middle">ELLERY'S</textPath></text>
      <text class="arch-face"><textPath href="#arch-path" startOffset="50%" text-anchor="middle">ELLERY'S</textPath></text>
    </svg>

    <div class="event-row">
      <span class="event-row__side">SEPT</span>
      <span class="event-row__main">DASH</span>
      <span class="event-row__side">2023</span>
    </div>

    <div class="runners-art" role="img" aria-label="Illustration of a colourful crowd of runners dashing left to right"></div>

    <div class="info-frame"></div>
    <h2 class="info info--headline">Fun Run <span class="amp">&amp;</span> Party</h2>
    <div class="rule rule--one"></div>
    <p class="info info--date">Sunday 10<sup>th</sup> September</p>
    <div class="rule rule--two"></div>
    <p class="info info--anyday">Your way any day</p>
    <p class="info info--month">All of September</p>
    <p class="info info--register">Register or support a participant at</p>
    <div class="web-address">www.ellerysdash.com</div>

    <p class="supporters-label">PROUDLY SUPPORTED BY:</p>
    <div class="sponsors">
      <span class="sponsor sponsor--pantrio">pantrio</span>
      <span class="sponsor sponsor--cloudnest"><span class="sponsor__dot"></span>cloudnest</span>
      <span class="sponsor sponsor--kazemoto">KAZEMOTO</span>
      <span class="sponsor sponsor--signal">Signalwave</span>
      <span class="sponsor sponsor--maple">maple</span>
    </div>
  </main>
</body>
</html>
```